Bytemill - a software development company requires letter head

I currently have a business card and logo, I just need a nice looking letter head the matches the two. I will upload these Illustrator files.

I would like the letter head to be done in a current version of MS Word.

Please incorporate 'bytemill' as per the attached font and the logo.

Industry/Entity Type

Computer Software

Colors

Designer to choose colors to be used in the design.

Requirements
Must have
• Fits in with current design, sleek and professional. It will be used for quotations and tenders and documentation going to clients and potential clients.
• Would like to company logo up the top header and perhaps a watermark of the logo at the bottom right, a bit like the business card.
• Also it needs to be MS word.
• Please work with the color pallet from the attached files.

```html
<!DOCTYPE html>
<html lang="en">
<head>
<meta charset="utf-8">
<title>Bytemill Letterhead</title>
<link rel="stylesheet" href="https://fonts.googleapis.com/css2?family=Raleway:wght@400;500;600&display=swap">
<style>
  :root {
    --brand-blue: #29abe2;
    --pendant-blue: #9fd8f2;
    --ink: #3c3c3c;
    --rule: #4a4a4a;
    --ghost: #e6e8ea;
    --canvas: #f1f0ed;
    --paper: #ffffff;
  }
  * { box-sizing: border-box; margin: 0; padding: 0; }
  html, body {
    width: 1000px;
    height: 1200px;
    overflow: hidden;
    background: var(--canvas);
    font-family: "Raleway", Arial, sans-serif;
  }
  .letterhead {
    position: absolute;
    left: 104px;
    top: 40px;
    width: 792px;
    height: 1120px;
    background: var(--paper);
    border: 6px solid var(--brand-blue);
    overflow: hidden;
  }
  .header-pendants {
    position: absolute;
    left: 0;
    top: 0;
    width: 100%;
    height: 130px;
    background: linear-gradient(to bottom, rgba(159,216,242,0.45), rgba(159,216,242,0));
  }
  .brand {
    position: absolute;
    left: 78px;
    top: 72px;
    display: flex;
    align-items: center;
    gap: 12px;
  }
  .brand-dot {
    width: 30px;
    height: 30px;
    border-radius: 50%;
    background: var(--brand-blue);
  }
  .brand-name {
    font-size: 30px;
    font-weight: 600;
    letter-spacing: 2px;
    color: var(--ink);
    text-transform: uppercase;
  }
  .watermark {
    position: absolute;
    right: -60px;
    bottom: -40px;
    width: 240px;
    height: 240px;
    border-radius: 50%;
    background: var(--ghost);
  }
  .footer-rule {
    position: absolute;
    left: 0;
    top: 1060px;
    width: 100%;
    height: 14px;
  }
  .contact-bar {
    position: absolute;
    left: 0;
    top: 1078px;
    width: 100%;
    display: flex;
    justify-content: center;
    gap: 82px;
    font-size: 12.5px;
    color: var(--ink);
  }
  .contact-item {
    display: flex;
    align-items: flex-start;
    gap: 10px;
    line-height: 1.25;
  }
  .contact-icon { width: 13px; height: 13px; margin-top: 1px; flex: none; }
</style>
</head>
<body>
  <main class="letterhead">
    <div class="header-pendants" role="img" aria-label="Row of thin light blue lines hanging from the top edge, each ending in a small circle"></div>

    <div class="brand">
      <span class="brand-dot"></span>
      <span class="brand-name">Bytemill</span>
    </div>

    <div class="watermark" aria-hidden="true"></div>

    <svg class="footer-rule" viewBox="0 0 780 14" preserveAspectRatio="none" aria-hidden="true">
      <line x1="0" y1="7" x2="380" y2="7" stroke="#4a4a4a" stroke-width="1.5"/>
      <circle cx="386" cy="7" r="5" fill="#fff" stroke="#4a4a4a" stroke-width="1.5"/>
      <circle cx="404" cy="7" r="5" fill="#fff" stroke="#4a4a4a" stroke-width="1.5"/>
      <line x1="410" y1="7" x2="780" y2="7" stroke="#4a4a4a" stroke-width="1.5"/>
    </svg>

    <footer class="contact-bar">
      <div class="contact-item">
        <svg class="contact-icon" viewBox="0 0 16 16" aria-hidden="true">
          <circle cx="8" cy="8" r="8" fill="#29abe2"/>
          <path d="M5 4.5c.6-.5 1.2-.4 1.5.2l.6 1.2c.2.4 0 .8-.3 1l-.5.4c.4.9 1.1 1.6 2 2l.4-.5c.3-.3.7-.4 1-.2l1.2.6c.6.3.7.9.2 1.5-.9 1-2.6.9-4.3-.7C5 8.4 4 6 5 4.5z" fill="#fff"/>
        </svg>
        <span>+61 400 317 208</span>
      </div>
      <div class="contact-item">
        <svg class="contact-icon" viewBox="0 0 16 16" aria-hidden="true">
          <circle cx="8" cy="8" r="8" fill="#29abe2"/>
          <path d="M8 3.5a3 3 0 0 0-3 3c0 2.2 3 5.8 3 5.8s3-3.6 3-5.8a3 3 0 0 0-3-3z" fill="#fff"/>
          <circle cx="8" cy="6.5" r="1.1" fill="#29abe2"/>
        </svg>
        <span>PO Box 218<br>Northfield SA 5085</span>
      </div>
      <div class="contact-item">
        <svg class="contact-icon" viewBox="0 0 16 16" aria-hidden="true">
          <circle cx="8" cy="8" r="8" fill="#29abe2"/>
          <rect x="4" y="5" width="8" height="6" rx="1" fill="#fff"/>
          <path d="M4.3 5.4L8 8.2l3.7-2.8" fill="none" stroke="#29abe2" stroke-width="1"/>
        </svg>
        <span>hello@bytemill.co</span>
      </div>
    </footer>
  </main>
</body>
</html>
```